MapleTrove shopping service flyer

We are a Korean shopping service. The attached picture explains our service. We would like to create a postcard or slightly larger sized flyer advertising our service. Front side will be graphics and back side text. For the front side, we want an updated version of the attached picture with our new logo and colours. And for the back side, create a simple design on the back side which we can enter all the text. Need font and design options.

Target Market(s)

20s and 30s females shopping for clothing (people not in Korea), shoppers are not Korean.

Industry/Entity Type

Online Shopping

Requirements
Must have
• For the front side, we want an updated version of the attached picture with our new logo and colours. And for the back side, create a simple design on the back side which we can enter all the text. Need font and design options.
Nice to have
• Little to no text on the front side.

```html
<!DOCTYPE html>
<html lang="en">
<head>
<meta charset="utf-8">
<title>MapleTrove shopping service flyer</title>
<link rel="stylesheet" href="https://fonts.googleapis.com/css2?family=Bebas+Neue&family=Lato:wght@400;700;900&display=swap">
<style>
  :root {
    --teal-deep: #1f9b8c;
    --teal-soft: #53bfae;
    --teal-pale: #a8dcd3;
    --orange: #e8784f;
    --ink: #141414;
    --paper: #f4f4f4;
    --paper-shade: #e3e3e3;
    --rule: #bdbdbd;
    --stage: #5e5e5e;
  }
  * { margin: 0; padding: 0; box-sizing: border-box; }
  html, body { width: 966px; height: 1200px; overflow: hidden; }
  body { background: var(--stage); font-family: "Lato", sans-serif; color: var(--ink); position: relative; }

  .card { position: absolute; left: 173px; width: 620px; height: 440px; overflow: hidden; background: var(--paper); }
  .card-front { top: 130px; }
  .card-back { top: 630px; }
  .card > * { position: absolute; }
  .card-bg { left: 0; top: 0; width: 620px; height: 440px; }

  .wordmark { font-family: "Lato", sans-serif; font-weight: 900; letter-spacing: -0.5px; line-height: 1; white-space: nowrap; }
  .front-wordmark { left: 192px; top: 104px; width: 222px; text-align: center; font-size: 34px; color: #fff; }
  .back-wordmark { left: 118px; top: 48px; font-size: 30px; color: var(--teal-deep); }
  .wordmark-dot { display: inline-block; width: 11px; height: 11px; background: var(--ink); border-radius: 50%; margin-right: 7px; vertical-align: middle; }
  .front-wordmark .wordmark-dot { background: #fff; }

  .art { border-radius: 8px; }
  .art-customer { left: 74px; top: 95px; width: 66px; height: 78px; background: linear-gradient(#ffffff, #e6f3f1); border-radius: 33px 33px 12px 12px; }
  .art-shops { left: 432px; top: 88px; width: 154px; height: 82px; background: linear-gradient(#f2a98c 0 22%, #cfe9e4 22%); }

  .pill { color: #fff; font-weight: 700; font-size: 10.5px; border-radius: 9px; height: 18px; line-height: 18px; text-align: center; background: #5cbcae; }
  .pill-customer { left: 56px; top: 185px; width: 96px; }
  .pill-shops { left: 459px; top: 185px; width: 96px; }

  .url-tab { height: 24px; line-height: 24px; color: #fff; font-weight: 900; font-size: 17px; letter-spacing: 0.8px; text-align: center; background: var(--orange); clip-path: polygon(3% 0, 100% 0, 97% 100%, 0 100%); }
  .url-tab .url-dot { display: inline-block; width: 11px; height: 11px; background: #fff; border-radius: 50%; margin-right: 8px; vertical-align: -1px; }
  .front-url { left: 196px; top: 233px; width: 236px; }
  .back-url { left: 185px; top: 387px; width: 236px; }

  .step-art { width: 78px; height: 60px; }
  .art-request { left: 66px; top: 297px; width: 40px; height: 72px; background: linear-gradient(#eef4f8, #2c8fd0); }
  .art-shopping { left: 200px; top: 310px; background: linear-gradient(#f2a98c 0 25%, #2aa394 25%); }
  .art-receive { left: 348px; top: 305px; background: linear-gradient(135deg, #f2a98c, #e8784f 60%, #2aa394); }
  .art-shipping { left: 500px; top: 306px; background: linear-gradient(90deg, #e8784f 0 40%, #d8a865 40%); }

  .step-label { width: 120px; text-align: center; font-size: 11px; line-height: 16px; text-transform: uppercase; color: #222; }
  .label-request { left: 28px; top: 392px; }
  .label-shopping { left: 173px; top: 392px; }
  .label-receive { left: 327px; top: 392px; }
  .label-shipping { left: 481px; top: 392px; }

  .address-line { left: 344px; width: 240px; height: 1px; background: var(--rule); }
  .line-1 { top: 37px; } .line-2 { top: 70px; } .line-3 { top: 102px; }

  .headline { left: 0; width: 620px; top: 126px; text-align: center; font-family: "Bebas Neue", sans-serif; font-size: 40px; font-weight: 400; line-height: 1; color: var(--ink); }
  .subline { left: 0; width: 620px; top: 170px; text-align: center; font-size: 17px; color: var(--ink); }

  .provide-tab { left: 21px; top: 231px; width: 200px; height: 23px; line-height: 23px; padding-left: 16px; background: var(--orange); color: #fff; font-size: 16px; font-weight: 700; letter-spacing: 1.4px; clip-path: polygon(0 0, 100% 0, 96% 100%, 0 100%); }
  .benefits { left: 22px; top: 262px; list-style: none; }
  .benefits li { display: flex; align-items: center; height: 29.5px; color: #fff; font-size: 14.5px; font-weight: 700; white-space: nowrap; }
  .tick { width: 17px; height: 17px; background: var(--orange); border-radius: 2px; margin-right: 14px; flex: none; }
  .follow { left: 23px; top: 356px; font-size: 11.5px; font-weight: 700; color: var(--ink); white-space: nowrap; }
  .follow .handle { color: var(--orange); }
  .handle-square { display: inline-block; width: 10px; height: 10px; background: var(--orange); border-radius: 2px; margin: 0 3px 0 4px; vertical-align: -1px; }
  .refund-note { left: 0; width: 620px; top: 416px; text-align: center; font-size: 9px; font-weight: 700; color: #fff; }
</style>
</head>
<body>

<section class="card card-front" aria-label="Flyer front">
  <svg class="card-bg" viewBox="0 0 620 440" aria-hidden="true">
    <defs>
      <linearGradient id="front-floor" x1="0" y1="0" x2="0" y2="1">
        <stop offset="0" stop-color="#fafafa"/><stop offset="1" stop-color="#e1e1e1"/>
      </linearGradient>
    </defs>
    <rect width="620" height="440" fill="url(#front-floor)"/>
    <path d="M0 0H620V226Q310 320 0 222Z" fill="var(--teal-deep)"/>
    <path d="M0 230Q310 330 620 232" fill="none" stroke="#fff" stroke-width="5"/>
    <g fill="none" stroke="#4fb9aa" stroke-width="2.5">
      <path d="M44 372A51 51 0 1 1 136 362"/>
      <path d="M189 372A51 51 0 1 1 281 362"/>
      <path d="M343 372A51 51 0 1 1 435 362"/>
      <path d="M497 372A51 51 0 1 1 589 362"/>
    </g>
    <g fill="none" stroke="#9a9a9a" stroke-width="1" stroke-dasharray="2 3">
      <path d="M136 360Q160 372 178 358"/>
      <path d="M290 318Q306 300 330 310"/>
      <path d="M444 360Q464 372 486 356"/>
    </g>
  </svg>

  <div class="art art-customer" role="img" aria-label="Icon of a customer"></div>
  <div class="pill pill-customer">CUSTOMER</div>

  <div class="wordmark front-wordmark"><span class="wordmark-dot"></span>MapleTrove</div>

  <div class="art art-shops" role="img" aria-label="Illustration of three online shop screens with striped awnings"></div>
  <div class="pill pill-shops">ONLINE SHOPS</div>

  <div class="url-tab front-url"><span class="url-dot"></span>mapletrove.com</div>

  <div class="art art-request" role="img" aria-label="Phone with shopping receipt and pay now button"></div>
  <div class="art step-art art-shopping" role="img" aria-label="Online shop on a computer screen"></div>
  <div class="art step-art art-receive" role="img" aria-label="Shopping bags and boxes gathered together"></div>
  <div class="art step-art art-shipping" role="img" aria-label="Delivery truck carrying parcels"></div>

  <p class="step-label label-request">Request &amp;<br>Payment</p>
  <p class="step-label label-shopping">Shopping</p>
  <p class="step-label label-receive">Receive &amp;<br>Consolidate</p>
  <p class="step-label label-shipping">Shipping<br>Worldwide</p>
</section>

<section class="card card-back" aria-label="Flyer back">
  <svg class="card-bg" viewBox="0 0 620 440" aria-hidden="true">
    <rect width="620" height="440" fill="var(--paper)"/>
    <path d="M330 0H420Q180 120 0 160V120Q150 80 330 0Z" fill="#fafafa"/>
    <path d="M0 168Q120 232 280 238Q460 240 620 134V440H0Z" fill="var(--teal-soft)"/>
    <path d="M0 168Q60 205 150 222Q60 222 0 210Z" fill="var(--teal-pale)"/>
  </svg>

  <div class="wordmark back-wordmark"><span class="wordmark-dot"></span>MapleTrove</div>

  <div class="address-line line-1"></div>
  <div class="address-line line-2"></div>
  <div class="address-line line-3"></div>

  <h1 class="headline">The Fastest Korean Shopping Service</h1>
  <p class="subline">GET THE HOTTEST TRENDING PRODUCTS FIRST</p>

  <div class="provide-tab">WE PROVIDE:</div>
  <ul class="benefits">
    <li><svg class="tick" viewBox="0 0 17 17" aria-hidden="true"><path d="M4 9l3 3 6-7" fill="none" stroke="#fff" stroke-width="2.4"/></svg>A QUICK TURN AROUND</li>
    <li><svg class="tick" viewBox="0 0 17 17" aria-hidden="true"><path d="M4 9l3 3 6-7" fill="none" stroke="#fff" stroke-width="2.4"/></svg>THE FASTEST SHIPPING OPTIONS</li>
    <li><svg class="tick" viewBox="0 0 17 17" aria-hidden="true"><path d="M4 9l3 3 6-7" fill="none" stroke="#fff" stroke-width="2.4"/></svg>A GUARANTEE YOU WILL GET THE ITEMS YOU REQUEST OR YOUR MONEY BACK*</li>
  </ul>

  <p class="follow">FOLLOW <span class="handle-square"></span><span class="handle">@MAPLETROVE</span> ON SOCIAL TO SEE MORE UNIQUE ITEMS AVAILABLE FROM KOREA!</p>

  <div class="url-tab back-url"><span class="url-dot"></span>mapletrove.com</div>
  <p class="refund-note">*refunds are on a product by product basis.</p>
</section>

</body>
</html>
```